Stonebell Inc Ad Design, trying to attract new customers

Please see attached pictures and files for information
We are a Class A - Residential General Contractor in Lynchburg, VA with Master HVAC and Master PLUMBING Licenses. We focus on Water and Air Solutions for property owners.
We build, remodel, and repair homes
We do HVAC, including Humidity Control and Air Purification
We do Plumbing
We love to fix Water Leaks for Plumbing, Roof Leaks, Skylight Leaks, Basement Leaks, Foundation Leaks, Door and Window Leaks
We solve water and air issues on the outside of properties with custom structures, grading, and landscaping

Target Market(s)

Residential and Light Commercial property owners

Industry/Entity Type

Construction

Font styles to use
Other font styles liked:
• see cards

Colors
0054AA
0677BA
7BADD7
CADEEF
E8F1F8
00AB8E
00BBA5
67D7C9
C6EFE9
E9F9F6

Requirements
Must have
• See business cards
Nice to have
• see business cards
Should not have
• My name

```html
<!DOCTYPE html>
<html lang="en">
<head>
<meta charset="utf-8">
<title>Stonebell Inc – Banner</title>
<link rel="stylesheet" href="https://fonts.googleapis.com/css2?family=Saira:wdth,wght@125,600;125,700;125,800&family=Open+Sans:wght@400;600&display=swap">
<style>
  :root{
    --page:#e2e2e2;
    --white:#ffffff;
    --blue-deep:#0677ba;
    --blue-bright:#0a9be6;
    --blue-light:#2fb0f0;
    --green-deep:#1f7a3c;
    --green:#2f9a3f;
    --green-light:#5cc04a;
    --black:#111111;
    --ink:#1d1d1d;
    --divider:#c9c9c9;
    --tick:#1a86d6;
    --tick-green:#3aa845;
  }
  *{margin:0;padding:0;box-sizing:border-box}
  html,body{width:1200px;height:392px;overflow:hidden;background:var(--page)}
  .stage{position:relative;width:1200px;height:392px;}
  .banner{position:absolute;left:120px;top:56px;width:960px;height:280px;background:var(--white);overflow:hidden;font-family:"Saira",sans-serif;font-stretch:125%}
  .banner-shapes{position:absolute;inset:0}
  .headline{position:absolute;left:34px;top:14px;color:var(--white);font-weight:800;font-size:41px;line-height:41px;letter-spacing:.5px}
  .headline .amp{font-weight:600}
  .license-tag{position:absolute;left:312px;top:60px;color:var(--white);font-weight:700;font-size:19px;line-height:30px;letter-spacing:.3px}
  .services{position:absolute;left:0;top:106px;height:31px;display:flex;align-items:center}
  .service{position:absolute;display:flex;align-items:center;gap:8px;color:var(--white);font-weight:700;font-size:19px;white-space:nowrap}
  .service .tick{width:14px;height:14px}
  .service-sep{position:absolute;top:7px;width:1px;height:18px;background:#555}
  .brand{position:absolute;left:760px;top:64px;display:flex;align-items:center;gap:8px;color:var(--blue-deep);font-weight:800;font-size:23px;letter-spacing:.5px}
  .brand .dot{width:16px;height:16px;border-radius:50%;background:var(--green)}
  .features{position:absolute;left:0;top:154px;width:960px;height:50px}
  .feature{position:absolute;top:0;display:flex;gap:6px;font-family:"Open Sans",sans-serif;font-size:12.3px;line-height:15px;color:var(--ink)}
  .feature svg{flex:none;margin-top:2px;width:9px;height:9px}
  .feature-sep{position:absolute;top:2px;width:1px;height:44px;background:var(--divider)}
  .contact-bar{position:absolute;left:0;top:220px;width:960px;height:60px;background:linear-gradient(180deg,var(--green-light),var(--green) 55%,var(--green-deep))}
  .contact{position:absolute;top:0;height:60px;display:flex;align-items:center;gap:8px;color:var(--white);font-weight:700;font-size:27px;letter-spacing:.5px}
  .contact .icon{width:28px;height:28px;border-radius:50%;background:var(--tick);display:flex;align-items:center;justify-content:center}
  .contact-sep{position:absolute;left:354px;top:14px;width:1px;height:32px;background:rgba(255,255,255,.45)}
</style>
</head>
<body>
<div class="stage">
  <div class="banner">
    <svg class="banner-shapes" width="960" height="280" viewBox="0 0 960 280" aria-hidden="true">
      <defs>
        <linearGradient id="blueBand" x1="0" y1="0" x2="1" y2="1">
          <stop offset="0" stop-color="#0677ba"/>
          <stop offset="1" stop-color="#0a9be6"/>
        </linearGradient>
        <linearGradient id="greenTag" x1="0" y1="0" x2="0" y2="1">
          <stop offset="0" stop-color="#5cc04a"/>
          <stop offset="1" stop-color="#1f7a3c"/>
        </linearGradient>
      </defs>
      <polygon points="0,0 748,0 672,108 0,108" fill="url(#blueBand)"/>
      <polygon points="560,0 748,0 672,108 500,108" fill="#2fb0f0" opacity=".35"/>
      <polygon points="300,58 716,58 696,90 300,90" fill="url(#greenTag)"/>
      <polygon points="0,106 672,106 656,137 0,137" fill="#111111"/>
    </svg>

    <div class="headline">MASTER HVAC <span class="amp">&amp;</span> MASTER<br>PLUMBING</div>
    <div class="license-tag">LICENSES IN LYNCHBURG,VA</div>

    <div class="services">
      <div class="service" style="left:34px;top:0"><svg class="tick" viewBox="0 0 14 14"><circle cx="7" cy="7" r="7" fill="#3aa845"/><path d="M3.8 7.2l2.2 2.2 4.2-4.4" stroke="#fff" stroke-width="1.8" fill="none"/></svg>WE BUILD</div>
      <span class="service-sep" style="left:204px"></span>
      <div class="service" style="left:230px;top:0"><svg class="tick" viewBox="0 0 14 14"><circle cx="7" cy="7" r="7" fill="#3aa845"/><path d="M3.8 7.2l2.2 2.2 4.2-4.4" stroke="#fff" stroke-width="1.8" fill="none"/></svg>REMODEL</div>
      <span class="service-sep" style="left:398px"></span>
      <div class="service" style="left:424px;top:0"><svg class="tick" viewBox="0 0 14 14"><circle cx="7" cy="7" r="7" fill="#3aa845"/><path d="M3.8 7.2l2.2 2.2 4.2-4.4" stroke="#fff" stroke-width="1.8" fill="none"/></svg>REPAIR HOMES</div>
    </div>

    <div class="brand"><span class="dot"></span>STONEBELL</div>

    <div class="features">
      <div class="feature" style="left:34px"><svg viewBox="0 0 10 10"><circle cx="5" cy="5" r="5" fill="#1a86d6"/><path d="M2.7 5.1l1.6 1.6 3-3.2" stroke="#fff" stroke-width="1.3" fill="none"/></svg><span>HVAC, including<br>Humidity Control and<br>Air Purification, Plumbing</span></div>
      <span class="feature-sep" style="left:230px"></span>
      <div class="feature" style="left:260px"><svg viewBox="0 0 10 10"><circle cx="5" cy="5" r="5" fill="#1a86d6"/><path d="M2.7 5.1l1.6 1.6 3-3.2" stroke="#fff" stroke-width="1.3" fill="none"/></svg><span>We focus on water<br>and air solutions<br>for property owners</span></div>
      <span class="feature-sep" style="left:432px"></span>
      <div class="feature" style="left:456px"><svg viewBox="0 0 10 10"><circle cx="5" cy="5" r="5" fill="#1a86d6"/><path d="M2.7 5.1l1.6 1.6 3-3.2" stroke="#fff" stroke-width="1.3" fill="none"/></svg><span>Custom structures,<br>grading, and<br>landscaping</span></div>
      <span class="feature-sep" style="left:626px"></span>
      <div class="feature" style="left:648px"><svg viewBox="0 0 10 10"><circle cx="5" cy="5" r="5" fill="#1a86d6"/><path d="M2.7 5.1l1.6 1.6 3-3.2" stroke="#fff" stroke-width="1.3" fill="none"/></svg><span>We fix Water Leaks for Plumbing, Roof Leaks,<br>Skylight Leaks, Basement Leaks, Foundation<br>Leaks, Door and Window Leaks</span></div>
    </div>

    <div class="contact-bar">
      <div class="contact" style="left:34px">
        <span class="icon"><svg width="16" height="16" viewBox="0 0 24 24"><path d="M6.6 10.8a15.2 15.2 0 0 0 6.6 6.6l2.2-2.2a1 1 0 0 1 1-.25 11.4 11.4 0 0 0 3.6.57 1 1 0 0 1 1 1V20a1 1 0 0 1-1 1A17 17 0 0 1 3 4a1 1 0 0 1 1-1h3.5a1 1 0 0 1 1 1c0 1.25.2 2.45.57 3.6a1 1 0 0 1-.25 1z" fill="#fff"/></svg></span>
        (434)555-0182
      </div>
      <span class="contact-sep"></span>
      <div class="contact" style="left:374px">
        <span class="icon"><svg width="16" height="16" viewBox="0 0 24 24" fill="none" stroke="#fff" stroke-width="2"><circle cx="12" cy="12" r="9"/><path d="M3 12h18M12 3c3 3 3 15 0 18M12 3c-3 3-3 15 0 18"/></svg></span>
        www.ShadeCrestVA.com
      </div>
    </div>
  </div>
</div>
</body>
</html>
```